Webdesign für Automotive Engineering Webpage
Automotive Engineering - Main focus is Software Development & Embedded systems for the Automotive industry.
Like as HMI, ADAS, ECU
See Logo (PDF), example --> https://www.brantlex.com/de/de (competetor)

```html
<!DOCTYPE html>
<html lang="de">
<head>
<meta charset="utf-8">
<title>VELTRAX – Automotive Engineering &amp; Consulting Solutions</title>
<link href="https://fonts.googleapis.com/css2?family=Lato:wght@400;700&family=Red+Hat+Display:wght@500;700&display=swap" rel="stylesheet">
<style>
:root{
  --navy:#062a5c;
  --red:#e01a22;
  --text:#3a3f4a;
  --white:#ffffff;
  --muted:#8a93a6;
  --head:"Red Hat Display",Arial,sans-serif;
  --body:"Lato",Arial,sans-serif;
}
*{margin:0;padding:0;box-sizing:border-box}
html,body{width:1200px;height:4197px;overflow:hidden;background:var(--white)}
body{font-family:var(--body);color:var(--text);position:relative}
section,header,nav,footer{position:relative;width:1200px;overflow:hidden}
.abs{position:absolute}
h2{font-family:var(--head);font-weight:700;font-size:29px;color:var(--navy);line-height:1.2}
h2 em{font-style:normal;color:var(--red)}
.on-dark h2{color:var(--white)}
.copy{font-size:12.6px;line-height:18px}
.copy p{margin-bottom:18px}
.on-dark .copy{color:#e6ebf3}

.topbar{height:91px;background:var(--navy)}
.topbar .rule{left:45px;right:45px;top:89px;height:2px;background:#2b4a78}
.burger{left:88px;top:33px;width:28px}
.burger span{display:block;height:3px;background:var(--red);margin-bottom:6px}
.brand{left:0;width:1200px;top:30px;text-align:center;font-family:var(--body);font-weight:700;font-size:30px;letter-spacing:3px;color:var(--white)}
.search{left:1082px;top:30px}

.mainnav{height:57px;background:var(--white)}
.mainnav a{position:absolute;top:18px;font-family:var(--body);font-size:19px;color:var(--navy);text-decoration:none;letter-spacing:.3px}
.mainnav a.active::after{content:"";position:absolute;left:0;right:0;top:33px;height:5px;background:var(--red)}

.hero{height:601px}
.hero .photo{inset:0;background:radial-gradient(ellipse at 55% 70%,#8fa3b6 0%,#5a6a80 35%,#2f3a4b 80%)}
.hero .band{left:0;right:0;top:108px;height:237px;background:rgba(30,44,70,.55)}
.hero h1{left:0;width:1200px;top:138px;text-align:center;font-family:var(--head);font-weight:700;font-size:48px;line-height:56px;color:var(--white)}
.hero .cta{left:500px;top:275px;width:200px;height:37px;border:1.5px solid #c8d0dc;border-radius:3px;color:#e7ecf2;font-size:12px;letter-spacing:1.8px;text-align:center;line-height:34px}

.services{height:570px}
.services h2{left:83px;top:70px}
.card{width:256px;height:256px;box-shadow:0 4px 14px rgba(0,0,0,.18)}
.card .img{position:absolute;left:0;top:0;width:256px;height:256px}
.card .cap{position:absolute;left:0;bottom:0;width:256px;height:88px;background:rgba(224,26,34,.9);padding:14px 15px;color:var(--white)}
.card .cap strong{display:block;font-size:14px;font-weight:700;margin-bottom:4px}
.card .cap span{display:block;font-size:12.5px;line-height:17px;color:#ffd9db}

.originate{height:465px;background:var(--navy)}
.originate h2{left:83px;top:70px}
.originate .copy{left:83px;top:138px;width:600px}
.originate .img{left:765px;top:135px;width:288px;height:231px;background:linear-gradient(135deg,#1f4f7e,#0d2c4f 60%,#3a86b8)}

.who{height:544px}
.who h2{left:83px;top:69px}
.who .copy{left:83px;top:137px;width:555px}
.who .img{left:700px;top:104px;width:480px;height:440px;background:linear-gradient(180deg,#f4f5f7 0%,#c9ced6 45%,#33456e 100%);border-radius:46% 46% 0 0}

.core{height:591px;background:var(--navy)}
.core .img{left:0;top:0;width:480px;height:591px;background:linear-gradient(135deg,#5d6470 0%,#9aa08a 45%,#c7c23e 60%,#3d4450 100%)}
.core h2{left:558px;top:60px;line-height:35px}
.core .copy{left:558px;top:161px;width:560px}

.openings{height:510px}
.openings h2{left:83px;top:70px}
.openings .slot{left:0;width:1200px;top:242px;text-align:center;font-family:var(--head);font-weight:700;font-size:24px;color:var(--navy)}

.contact{height:454px;background:var(--navy)}
.contact .kicker{left:99px;top:79px;font-size:11.5px;letter-spacing:2px;color:#9aa9c2}
.contact h2{left:99px;top:110px;width:490px;line-height:36px;font-weight:500}
.contact .lead{left:99px;top:237px;width:370px;font-size:12.6px;line-height:18px;color:#e6ebf3}
.field{left:651px;width:466px;height:37px;background:var(--white);border-radius:2px;padding:11px 13px;font-size:12.5px;color:var(--muted)}
.send{left:651px;top:332px;width:183px;height:37px;background:var(--red);color:var(--white);font-size:11.5px;letter-spacing:2px;text-align:center;line-height:37px;border-radius:2px}

.site-footer{height:267px;background:var(--white)}
.site-footer .brand-foot{left:99px;top:86px;font-family:var(--body);font-weight:700;font-size:30px;letter-spacing:3px;color:var(--navy)}
.socials{left:101px;top:164px;display:flex;gap:15px}
.socials span{width:22px;height:22px;border-radius:4px;background:var(--navy);display:block}
.col{top:60px}
.col h4{font-size:13.5px;font-weight:700;color:#222;margin-bottom:14px}
.col li{list-style:none;font-size:12.5px;color:#333;line-height:27px}
.addr li{display:flex;gap:12px;line-height:18px;margin-bottom:4px;font-size:11.6px}
.addr svg{flex:none;margin-top:2px}

.legal{position:relative;width:1200px;height:47px;background:var(--red);color:var(--white);font-size:11.5px}
.legal .left{left:83px;top:16px}
.legal .right{right:85px;top:16px}
</style>
</head>
<body>

<header class="topbar">
  <div class="abs burger"><span></span><span></span><span></span></div>
  <div class="abs brand">VELTRAX</div>
  <svg class="abs search" width="30" height="30" viewBox="0 0 30 30" aria-label="Suche"><circle cx="12" cy="12" r="9" fill="none" stroke="#fff" stroke-width="3"/><line x1="18.5" y1="18.5" x2="27" y2="27" stroke="#fff" stroke-width="3.5" stroke-linecap="round"/></svg>
  <div class="abs rule"></div>
</header>

<nav class="mainnav">
  <a class="active" style="left:172px">ÜBER UNS</a>
  <a style="left:319px">UNSERE LEISTUNGEN</a>
  <a style="left:573px">BEWERBER</a>
  <a style="left:726px">OFFENE STELLEN</a>
  <a style="left:939px">KONTAKT</a>
</nav>

<section class="hero">
  <div class="abs photo" role="img" aria-label="Foto: Ingenieure arbeiten im Labor an einem Elektronik-Prototyp"></div>
  <div class="abs band"></div>
  <h1 class="abs">Automotive Engineering<br>&amp; Consulting Solutions</h1>
  <div class="abs cta">ZUR PROJEKTÜBERSICHT</div>
</section>

<section class="services">
  <h2 class="abs">Unsere <em>Leistungen</em></h2>
  <div class="abs card" style="left:172px;top:177px">
    <div class="img" role="img" aria-label="Foto: Mechaniker arbeiten an einem Fahrzeug in der Werkstatt" style="background:linear-gradient(160deg,#9aa3ae,#3c4a66 60%,#1d2a48)"></div>
    <div class="cap"><strong>Full Service Engineering</strong><span>Übernahme kompletter R&amp;D<br>Projekte als Fremdleistung</span></div>
  </div>
  <div class="abs card" style="left:472px;top:251px">
    <div class="img" role="img" aria-label="Foto: zwei Fachkräfte mit Schutzhelm" style="background:linear-gradient(160deg,#c9cdd2,#8d97a6 55%,#2e4068)"></div>
    <div class="cap"><strong>Premium Recruiting</strong><span>Vermittlung bis hin zum Onboarding<br>von Freelancern und Festangestellten</span></div>
  </div>
  <div class="abs card" style="left:772px;top:177px">
    <div class="img" role="img" aria-label="Foto: Ingenieurin mit Helm und Klemmbrett in einer Fabrikhalle" style="background:linear-gradient(160deg,#7f8a78,#55606c 55%,#2f4a7a)"></div>
    <div class="cap"><strong>Arbeitnehmerüberlassung</strong><span>Automotive R&amp;D Experten und<br>Ingenieure in Zeitarbeit</span></div>
  </div>
</section>

<section class="originate on-dark">
  <h2 class="abs">Originate in <em>Engineering</em></h2>
  <div class="abs copy">
    <p>Halvorsen Recruitment vereint in sich 25 Jahre Branchen- und Projekterfahrung vom Freelance Ingenieur bis zum Task Force Manager in den Branchen Automotive, Schienenfahrzeuge, Luft- und Raumfahrt, Rüstung und Informationstechnologie.</p>
    <p>Firmengründer und Geschäftsführer Jonas Halvorsen kennt die Industrie seit über zwei Jahrzehnten, in denen er in Positionen als IT Entwicklungsingenieur, Experte für Geodaten und rund um das Thema autonomes Fahren und Fahrassistenzsysteme, bis zum CIO und Task Force Manager bei fast allen wichtigen OEMs und Tier1s des Automotive Sektors und anderer Schlüsselindustrien Erfahrungen sammeln konnte.</p>
    <p>Wie der Firmengründer, so verfügen auch alle maßgeblichen Mitarbeiter bei Halvorsen Recruitment über diese Double Qualification – wir sprechen Ihre Sprache und wissen, wo Ihr Bedarf liegt, kennen Ihre Abläufe und Prozesse, sind aus eigener Erfahrung heraus im Geschäft.</p>
  </div>
  <div class="abs img" role="img" aria-label="Foto: Entwicklerin an Monitoren in einem Kontrollraum"></div>
</section>

<section class="who">
  <h2 class="abs">Wer wir <em>sind</em></h2>
  <div class="abs copy">
    <p>Halvorsen Recruitment vereint in sich 25 Jahre Branchen- und Projekterfahrung vom Freelance Ingenieur bis zum Task Force Manager in den Branchen Automotive, Schienenfahrzeuge, Luft- und Raumfahrt, Rüstung und Informationstechnologie.</p>
    <p>Firmengründer und Geschäftsführer Jonas Halvorsen kennt die Industrie seit über zwei Jahrzehnten, in denen er in Positionen als IT Entwicklungsingenieur, Experte für Geodaten und rund um das Thema autonomes Fahren und Fahrassistenzsysteme, bis zum CIO und Task Force Manager bei fast allen wichtigen OEMs und Tier1s des Automotive Sektors und anderer Schlüsselindustrien Erfahrungen sammeln konnte.</p>
    <p>Wie der Firmengründer, so verfügen auch alle maßgeblichen Mitarbeiter bei Halvorsen Recruitment über diese Double Qualification. Sie sprechen mit Fachleuten und Kollegen, nicht mit reinen Recruitern!</p>
    <p>Wir wissen, wo der Bedarf unserer Kunden liegt, kennen deren Abläufe und Prozesse, sind aus eigener Erfahrung heraus im Geschäft.</p>
  </div>
  <div class="abs img" role="img" aria-label="Foto: zwei Mechaniker in Latzhosen, einer mit Klemmbrett"></div>
</section>

<section class="core on-dark">
  <div class="abs img" role="img" aria-label="Foto: Techniker montiert eine Bremsscheibe an einer Achse"></div>
  <h2 class="abs">Konzentrieren Sie sich auf Ihre<br><em>Kernkompetenzen</em></h2>
  <div class="abs copy">
    <p>Ihr Wissen, Ihre Erfahrung und Ihr Können sind wertvolle Assets. Sie brauchen nur noch die richtigen Verbindungen, um eine finanziell wie emotional befriedigende Arbeit daraus zu kreieren. Genau für letzteres können Sie uns ansprechen. Wir kennen Ihre Situation und Ihre Wünsche aus eigenen, langjährigen Erfahrungen, denn wir kommen aus dem IT- und Engineering-Bereich. Wir haben selbst als Freelancer in Automotive und anderen Schlüsselindustrien gearbeitet und wissen, was Sie suchen!</p>
    <p>Wir vermitteln Sie als Freelancer oder festangestellt projekt- oder zeitbezogen an Ihre Wunschpartner in der Industrie. Wenn Sie in einem festen Arbeitsverhältnis oder im Rahmen einer Arbeitnehmerüberlassung angestellt werden wollen, können Sie uns ebenfalls ansprechen. Wir arbeiten zudem international mit den führenden OEMs, Tier-1 und Tier-2 Unternehmen der Automobilindustrie zusammen.</p>
    <p>Aber bevor Sie uns gleich Ihre Unterlagen schicken, nehmen Sie kurz Kontakt mit uns auf, damit von Anfang an alles passt. Unsere Arbeit lebt von Effektivität und Effizienz und wir wollen weder Ihre, noch die Zeit unserer Kunden mit offenen Fragen oder gar Nachbesserungen verschwenden!</p>
    <p>Sie wollen sich initativ bewerben? Schicken Sie uns bitte Ihre Unterlagen an cv@halvorsen-recruitment.de</p>
  </div>
</section>

<section class="openings">
  <h2 class="abs">Offene <em>Stellen</em></h2>
  <div class="abs slot">Hier das Add-in aus Linkora einfügen für Vakanzen und Ausschreibungen</div>
</section>

<section class="contact on-dark">
  <div class="abs kicker">HALVORSEN RECRUITMENT GMBH</div>
  <h2 class="abs">Sie suchen Spezialisten für eine bestimmte Aufgabe, oder möchten mit uns in Kontakt treten?</h2>
  <p class="abs lead">Senden Sie uns zum Beispiel Ihre Anforderungen und wir kommen mit passenden Profilen auf Sie zu, oder nehmen Sie einfach mit uns Kontakt auf und erfahren was wir für Sie tun können.</p>
  <div class="abs field" style="top:101px">Name*</div>
  <div class="abs field" style="top:158px">E-Mail*</div>
  <div class="abs field" style="top:216px">Telefonnummer</div>
  <div class="abs field" style="top:273px">Ort/PLZ*</div>
  <div class="abs send">ANFRAGE ABSENDEN</div>
</section>

<footer class="site-footer">
  <div class="abs brand-foot">VELTRAX</div>
  <div class="abs socials"><span></span><span></span><span></span><span></span></div>
  <div class="abs col" style="left:386px">
    <h4>Navigation</h4>
    <ul><li>Über uns</li><li>Unsere Leistungen</li><li>Bewerber</li><li>Offene Stellen</li><li>Kontakt</li></ul>
  </div>
  <div class="abs col" style="left:637px">
    <h4>Kundenservice</h4>
    <ul><li>Registrieren</li><li>Impressum</li><li>Datenschutz</li></ul>
  </div>
  <div class="abs col addr" style="left:887px">
    <h4>Adresse &amp; Kontakt</h4>
    <ul>
      <li><svg width="14" height="16" viewBox="0 0 14 16"><path d="M7 1a5 5 0 0 0-5 5c0 4 5 9 5 9s5-5 5-9a5 5 0 0 0-5-5z" fill="#b3bccb"/><circle cx="7" cy="6" r="2" fill="#fff"/></svg><span>Lindenstraße 24<br>D - 34123 Talbrück (OT Ahrfeld)</span></li>
      <li><svg width="14" height="14" viewBox="0 0 14 14"><path d="M3 1l3 3-1.5 2a8 8 0 0 0 3.5 3.5L10 8l3 3-2 2C6 13 1 8 1 3z" fill="#b3bccb"/></svg><span>+49 (0)5671 -312 40 18</span></li>
      <li><svg width="14" height="14" viewBox="0 0 14 14"><rect x="3" y="1" width="8" height="4" fill="#b3bccb"/><rect x="1" y="5" width="12" height="5" rx="1" fill="#b3bccb"/><rect x="3" y="9" width="8" height="4" fill="#d5dbe4"/></svg><span>+49 (0)5671 -312 40 19</span></li>
      <li><svg width="14" height="12" viewBox="0 0 14 12"><rect x="0" y="1" width="14" height="10" rx="1" fill="#b3bccb"/><path d="M0 2l7 5 7-5" fill="none" stroke="#fff" stroke-width="1.3"/></svg><span>office@halvorsen-recruitment.de<br>D-U-N-S Nr. 517208936</span></li>
    </ul>
  </div>
</footer>

<div class="legal">
  <span class="abs left">© 2020 veltrax.com | All rights reserved.</span>
  <span class="abs right">TremsOfUse &nbsp;Privacy</span>
</div>

</body>
</html>
```